Website Design - for Energy Efficiency company - large corporate feel

Hi there,
Thanks for checking out this project!
We're a UK based energy efficiency business. We arrange for energy efficient systems to be fitted in people's houses (i.e. efficient boilers, solar panels etc.) However, we do not install them ourselves as we have accredited installers who install on our behalf. Therefore the website should appeal to these businesses and have a very professional corporate feel. The final design should communicate that we are a financially safe large corporation.
Our existing website should not be used for inspiration as the style and content are very outdated (it was from a time when were installers - which we no longer are).
The new website design should use the greens from our logo, however I don't want the site saturated in this colour.
I'm really open to your chosen layout and therefore I'm not a huge fan of including links to websites I like - as I don't want to limit your own creativity. However, I would like it to look corporate (but not too boring and unimaginative).
So here's a few links to websites that I feel give a feel of financially safe / large corporate etc. Although you certainly don't have to design with this style / layout in mind:
http://www.brelvanhub.org.uk/advice
http://www.tolvenrise.co.uk/
http://www.qpwd.org.uk/
http://www.wendrowkeyplot.co.uk/
http://www.ruvasto.co.uk/ (very bad design but looks corporate)
http://www.pellarwatt.org.uk/
http://www.vq.co.uk/ (looks corporate but too busy and boring)
http://www.quellisto.co.uk/business/index.htm
http://www.dormavel.com/
https://www.ostrevan.com/en/index.html
The site is for 4 different audiences:
Consumers | Businesses | Public Sector | Installers
Therefore, it's important that there is some form of way of splitting the site up into these sections (almost like 4 websites in 1). Each section will then have the navigation menu with 7 links.
I've attached our logo (company-logo.jpg) and another logo design we have to display inline with regulations (blue-pact-logo.jpg).
Happy designing, and thank you!

```html
<!DOCTYPE html>
<html lang="en">
<head>
<meta charset="utf-8">
<title>Verdano Energy</title>
<link href="https://fonts.googleapis.com/css2?family=Arimo:wght@400;700&display=swap" rel="stylesheet">
<style>
  :root {
    --green: #7ab83a;
    --green-dark: #3f8f1f;
    --green-pale: #d4ebb0;
    --green-bar: #b2d86a;
    --charcoal: #3a3a3a;
    --charcoal-dark: #2f2f2f;
    --card: #f2f0f0;
    --text: #222;
    --muted: #777;
    --white: #fff;
  }
  * { box-sizing: border-box; margin: 0; padding: 0; }
  html, body { width: 1200px; height: 1023px; overflow: hidden; }
  body {
    position: relative;
    background: var(--charcoal);
    font-family: "Arimo", Arial, sans-serif;
    color: var(--text);
  }
  a { color: inherit; text-decoration: none; }

  .hero {
    position: absolute; left: 0; top: 0; width: 1200px; height: 330px;
    background:
      radial-gradient(ellipse at 20% 30%, rgba(255,255,255,.75), transparent 40%),
      radial-gradient(ellipse at 88% 25%, rgba(255,255,255,.7), transparent 35%),
      radial-gradient(ellipse at 60% 90%, rgba(255,255,255,.4), transparent 40%),
      linear-gradient(180deg, #e4f2c9 0%, #c9e49a 60%, #b8da7c 100%);
  }
  .hero::before {
    content: ""; position: absolute; left: 0; top: 0; width: 100%; height: 5px;
    background: var(--charcoal-dark);
  }
  .hero::after {
    content: ""; position: absolute; left: 802px; top: 0; width: 102px; height: 5px;
    background: var(--green-dark);
  }
  .lang { position: absolute; left: 819px; top: 10px; font-size: 7.5px; color: #666; word-spacing: 3px; }

  .brand { position: absolute; display: flex; align-items: center; gap: 7px; color: var(--green-dark); font-weight: 700; }
  .brand-mark { border-radius: 50%; background: var(--green-dark); }
  .brand--header { left: 304px; top: 24px; font-size: 26px; }
  .brand--header .brand-mark { width: 34px; height: 34px; }

  .intro { position: absolute; left: 304px; top: 108px; width: 250px; }
  .intro-title {
    width: 214px; height: 31px; background: var(--green-bar);
    font-size: 11.5px; font-weight: 400; line-height: 31px; padding-left: 18px; color: #2a3a12;
  }
  .intro-text { margin-top: 12px; font-size: 8.4px; line-height: 16px; }
  .intro-more { display: block; margin-top: 26px; font-size: 8.6px; color: #333; }

  .slider {
    position: absolute; left: 575px; top: 85px; width: 329px; height: 184px;
    background: var(--green-pale); padding: 5px;
  }
  .slider-photo { width: 100%; height: 100%; background: linear-gradient(180deg, #1f4fb5 0%, #3a7ad8 60%, #6da3e8 100%); }
  .slider-dots { position: absolute; left: 584px; top: 279px; display: flex; gap: 2px; }
  .slider-dots span { width: 8px; height: 8px; border-radius: 50%; background: var(--green); }
  .slider-dots span:first-child { background: var(--green-dark); }

  .main-nav {
    position: absolute; left: 304px; top: 298px; width: 600px; height: 33px;
    background: var(--charcoal); border-radius: 4px 4px 0 0;
    display: flex; align-items: center; padding-left: 18px; gap: 0;
  }
  .main-nav a { color: var(--white); font-size: 8.6px; padding: 0 9px; line-height: 20px; }
  .main-nav a.is-active {
    background: linear-gradient(180deg, #8cc84a, #5f9e25); border-radius: 3px; padding: 0 18px; margin-right: 0;
  }

  .content {
    position: absolute; left: 304px; top: 331px; width: 600px; height: 535px;
    background: var(--white); border-radius: 0 0 3px 3px;
  }
  .audiences { position: absolute; left: 18px; top: 26px; display: flex; gap: 4px; }
  .audience {
    width: 139px; height: 163px; background: var(--card); padding: 8px 7px;
    box-shadow: 0 6px 6px -4px rgba(0,0,0,.18);
  }
  .audience h3 { font-size: 11px; font-weight: 400; color: #333; margin-bottom: 8px; }
  .audience-photo { width: 120px; height: 64px; margin: 0 auto; border: 3px solid var(--white); }
  .audience-photo--consumers { background: linear-gradient(135deg, #4a9a2c, #2f7d1d); }
  .audience-photo--businesses { background: linear-gradient(135deg, #e8f0e0, #5ea33a); }
  .audience-photo--public { background: linear-gradient(135deg, #7fa86a, #cfd8cf); }
  .audience-badge { width: 120px; height: 64px; margin: 0 auto; background: #2d7a1f; border: 3px solid var(--white); }
  .audience p { margin-top: 12px; font-size: 6.8px; line-height: 8.6px; color: var(--muted); padding: 0 1px; }
  .audience a { display: block; margin-top: 8px; font-size: 6.6px; color: var(--green-dark); text-decoration: underline; }

  .welcome { position: absolute; left: 19px; top: 217px; width: 555px; }
  .welcome h2 { font-size: 13.5px; font-weight: 400; color: #333; }
  .welcome-lead { margin-top: 17px; font-size: 7.6px; line-height: 13px; }
  .welcome-photo {
    position: absolute; left: 18px; top: 293px; width: 203px; height: 140px;
    background: #f4f4f4; padding: 5px; box-shadow: 0 6px 6px -4px rgba(0,0,0,.2);
  }
  .welcome-photo div { width: 100%; height: 100%; background: linear-gradient(180deg, #cfe4b8 0%, #5f9a3a 55%, #2e5a1e 100%); }
  .welcome-body { position: absolute; left: 230px; top: 279px; width: 340px; font-size: 6.6px; line-height: 13px; }
  .welcome-body p { margin-bottom: 4px; }
  .welcome-body .highlight { color: var(--green-dark); }

  .footer { position: absolute; left: 304px; top: 893px; width: 600px; color: #ddd; }
  .footer h4 { font-size: 12.5px; font-weight: 400; color: var(--white); }
  .footer-about { position: absolute; left: 0; top: 0; width: 155px; }
  .footer-about p { margin-top: 10px; font-size: 6.6px; line-height: 13px; }
  .footer-about a { display: block; margin-top: 6px; font-size: 6.6px; text-decoration: underline; }
  .footer-links { position: absolute; top: 0; width: 100px; }
  .footer-links h4 { border-bottom: 1px solid #555; padding-bottom: 8px; }
  .footer-links ul { list-style: none; margin-top: 6px; }
  .footer-links li { font-size: 6.6px; line-height: 13px; padding-left: 2px; }
  .footer-links--one { left: 178px; }
  .footer-links--two { left: 311px; }
  .footer-meta { position: absolute; left: 448px; top: 25px; width: 160px; }
  .social { display: flex; gap: 4px; align-items: center; }
  .social span { width: 18px; height: 18px; border-radius: 50%; background: #8a8a8a; }
  .social .divider { width: 1px; height: 20px; border-radius: 0; background: #666; margin: 0 9px; }
  .brand--footer { position: static; color: var(--white); font-size: 13px; gap: 5px; }
  .brand--footer .brand-mark { width: 14px; height: 14px; background: var(--white); }
  .footer-copy { margin-top: 9px; font-size: 6px; color: #999; }
</style>
</head>
<body>
  <header class="hero">
    <div class="lang">English | Language</div>
    <div class="brand brand--header"><span class="brand-mark"></span>Verdano Energy</div>

    <section class="intro">
      <h1 class="intro-title">Lorem ipsum dolor sit amet</h1>
      <p class="intro-text">Lorem ipsum dolor sit amet, consectetur adipisicing elit, sed do eiusmod tempor incididunt ut labore et dolore magna aliqua. Ut enim ad minim veniam, quis nostrud exercitation ullamco laboris nisi ut aliquip ex ea commodo consequat.</p>
      <a class="intro-more" href="#">Learn More...</a>
    </section>

    <div class="slider">
      <div class="slider-photo" role="img" aria-label="Solar panel array on a pole against a blue sky"></div>
    </div>
    <div class="slider-dots"><span></span><span></span><span></span><span></span></div>
  </header>

  <nav class="main-nav">
    <a class="is-active" href="#">Home</a>
    <a href="#">About Us</a>
    <a href="#">Blue Pact</a>
    <a href="#">ECO</a>
    <a href="#">Landlords</a>
    <a href="#">Renewables</a>
    <a href="#">Contact Us</a>
  </nav>

  <main class="content">
    <div class="audiences">
      <article class="audience">
        <h3>Consumers</h3>
        <div class="audience-photo audience-photo--consumers" role="img" aria-label="Green recycling arrows"></div>
        <p>Lorem ipsum dolor sit amet, consectetur adipisicing elit, sed do eiusmod tempor incididunt</p>
        <a href="#">Read More &gt;&gt;</a>
      </article>
      <article class="audience">
        <h3>Businesses</h3>
        <div class="audience-photo audience-photo--businesses" role="img" aria-label="Pen resting on a financial chart"></div>
        <p>Lorem ipsum dolor sit amet, consectetur adipisicing elit, sed do eiusmod tempor incididunt</p>
        <a href="#">Read More &gt;&gt;</a>
      </article>
      <article class="audience">
        <h3>Public Sector</h3>
        <div class="audience-photo audience-photo--public" role="img" aria-label="Businesswoman standing by a window"></div>
        <p>Lorem ipsum dolor sit amet, consectetur adipisicing elit, sed do eiusmod tempor incididunt</p>
        <a href="#">Read More &gt;&gt;</a>
      </article>
      <article class="audience">
        <h3>Installers</h3>
        <div class="audience-badge" role="img" aria-label="Approved installer badge"></div>
        <p>Lorem ipsum dolor sit amet, consectetur adipisicing elit, sed do eiusmod tempor incididunt</p>
        <a href="#">Read More &gt;&gt;</a>
      </article>
    </div>

    <section class="welcome">
      <h2>Welcome to our Website</h2>
      <p class="welcome-lead">Lorem ipsum dolor sit amet, consectetur adipisicing elit, sed do eiusmod tempor incididunt ut labore et dolore magna aliqua. Ut enim ad minim veniam, quis nostrud exercitation ullamco laboris nisi ut aliquip ex ea commodo consequat.</p>
    </section>

    <figure class="welcome-photo">
      <div role="img" aria-label="Handshake between two business people in a green forest"></div>
    </figure>

    <div class="welcome-body">
      <p>Lorem ipsum dolor sit amet, consectetur adipisicing elit, sed do eiusmod tempor incididunt ut labore et dolore magna aliqua. Ut enim ad minim veniam, quis nostrud exercitation ullamco laboris nisi ut aliquip ex ea commodo consequat.</p>
      <p>Lorem ipsum dolor sit amet, consectetur adipisicing elit, sed do eiusmod tempor incididunt ut labore et dolore magna aliqua. Ut enim ad minim veniam, quis nostrud <span class="highlight">exercitation ullamco laboris nisi ut aliquip</span> ex ea commodo consequat.</p>
      <p>Lorem ipsum dolor sit amet, consectetur adipisicing elit, sed do eiusmod tempor incididunt ut labore et dolore magna aliqua. Ut enim ad minim veniam, quis nostrud exercitation.</p>
      <p>Lorem ipsum dolor sit amet, consectetur adipisicing elit, sed do eiusmod tempor incididunt ut labore et dolore magna aliqua. Ut enim ad minim veniam, quis nostrud exercitation ullamco laboris nisi ut aliquip ex ea commodo consequat. Duis aute irure dolor in reprehenderit in voluptate velit esse cillum dolore eu fugiat nulla pariatur. Excepteur sint occae-cat cupidatat non proident, sunt in culpa qui officia deserunt mollit anim id est laborum.</p>
    </div>
  </main>

  <footer class="footer">
    <section class="footer-about">
      <h4>Privacy Policy</h4>
      <p>Lorem ipsum dolor sit amet, consectetur adipisicing elit, sed do eiusmod tempor incididunt ut labore et dolore magna aliqua. Ut enim ad minim veniam, quis nostrud exercitation ullamco laboris nisi ut aliquip ex ea commodo consequat.</p>
      <a href="#">read more &gt;&gt;</a>
    </section>
    <section class="footer-links footer-links--one">
      <h4>Other Links</h4>
      <ul>
        <li>Lorem ipsum dolor</li><li>Lorem ipsum</li><li>Lorem ipsum dolor</li>
        <li>Lorem ipsum do</li><li>Lorem ipsum dolor</li><li>Lorem ipsum</li>
      </ul>
    </section>
    <section class="footer-links footer-links--two">
      <h4>Other Links</h4>
      <ul>
        <li>Lorem ipsum dolor</li><li>Lorem ipsum</li><li>Lorem ipsum dolor</li>
        <li>Lorem ipsum do</li><li>Lorem ipsum dolor</li><li>Lorem ipsum</li>
      </ul>
    </section>
    <div class="footer-meta">
      <div class="social">
        <span aria-label="Social link one"></span>
        <span aria-label="Social link two"></span>
        <span class="divider"></span>
        <div class="brand brand--footer"><span class="brand-mark"></span>Verdano Energy</div>
      </div>
      <p class="footer-copy">2013. All Right Reserved.</p>
    </div>
  </footer>
</body>
</html>
```